Strategic Plan Notecards (4.25in x 5.5 in)

I need a design for project cards that will be handed out to the general public as part of a Strategic Planning effort for a client. I'd like the cards to be 4.25 x 5.5 so that they can be printed 4 to a US letter-size sheet of paper.

The Project title is "City of Quellmont Strategic Plan Update"
Needs to include text:

For more info, go to www.quellmontfutures.example
Take the Vision Survey at http://lnk.example/QuellmontOutlook
What do you want Quellmont to be?

Other variations on this text will be considered.

Target Market(s)

General Public

Font styles to use
Serif
Sans Serif

Colors

Designer to choose colors to be used in the design.

Requirements
Must have
• An interesting and fun visual appeal. Nothing stuffy. Should have a bright graphic background and interesting typefaces for the text.
Nice to have
• One of the biggest assets in the community is the Missouri River - some depiction of a river would be great.

```html
<!DOCTYPE html>
<html lang="en">
<head>
<meta charset="utf-8">
<title>Quellmont Strategic Plan Notecard</title>
<link rel="stylesheet" href="https://fonts.googleapis.com/css2?family=Bebas+Neue&family=Lato:wght@400;900&family=Oswald:wght@200&display=swap">
<style>
  :root {
    --sun: #dcc31b;
    --sun-deep: #cdb315;
    --sun-light: #e6cf2c;
    --navy: #0b1838;
    --ink: #111111;
    --gold: #b9a213;
    --paper: #ffffff;
  }
  html, body {
    margin: 0;
    width: 917px;
    height: 1200px;
    overflow: hidden;
    background: var(--paper);
  }
  .notecard { display: block; width: 917px; height: 1200px; }
  .title-bold { font-family: "Bebas Neue", "Oswald", sans-serif; }
  .title-thin { font-family: "Oswald", sans-serif; font-weight: 200; }
  .question { font-family: "Lato", sans-serif; font-weight: 900; fill: var(--navy); }
  .survey-lead { font-family: "Lato", sans-serif; font-weight: 400; fill: var(--ink); }
  .survey-link { font-family: "Lato", sans-serif; font-weight: 900; fill: var(--gold); }
  .info-lead { font-family: "Bebas Neue", sans-serif; fill: var(--paper); }
  .info-link { font-family: "Bebas Neue", sans-serif; fill: var(--sun); }
</style>
</head>
<body>
<svg class="notecard" viewBox="0 0 917 1200" xmlns="http://www.w3.org/2000/svg">
  <defs>
    <linearGradient id="sun-wash" x1="0" y1="0" x2="1" y2="1">
      <stop offset="0" stop-color="var(--sun-deep)"/>
      <stop offset="0.5" stop-color="var(--sun-light)"/>
      <stop offset="1" stop-color="var(--sun)"/>
    </linearGradient>
  </defs>

  <!-- title band -->
  <rect class="title-band" x="0" y="0" width="917" height="725" fill="url(#sun-wash)" role="img" aria-label="Bright yellow low-poly faceted background pattern"/>

  <text class="title-bold" x="458" y="168" text-anchor="middle" font-size="158" fill="var(--navy)" textLength="331" lengthAdjust="spacingAndGlyphs">CITY OF</text>
  <text class="title-bold" x="458" y="369" text-anchor="middle" font-size="259" fill="var(--navy)" textLength="754" lengthAdjust="spacingAndGlyphs">QUELLMONT</text>
  <text class="title-bold" x="458" y="516" text-anchor="middle" font-size="163" fill="var(--ink)" textLength="744" lengthAdjust="spacingAndGlyphs">STRATEGIC PLAN</text>
  <text class="title-thin" x="91" y="684" font-size="166" fill="var(--ink)" textLength="734" lengthAdjust="spacing">UPDATE</text>

  <!-- survey panel -->
  <rect class="survey-panel" x="0" y="725" width="917" height="370" fill="var(--paper)"/>
  <text class="question" x="458" y="829" text-anchor="middle" font-size="79" textLength="778" lengthAdjust="spacingAndGlyphs">WHAT DO YOU WANT</text>
  <text class="question" x="458" y="908" text-anchor="middle" font-size="79">QUELLMONT TO BE?</text>
  <text class="survey-lead" x="458" y="999" text-anchor="middle" font-size="42">Take the Vision Survey at</text>
  <text class="survey-link" x="458" y="1060" text-anchor="middle" font-size="52" textLength="820" lengthAdjust="spacingAndGlyphs">HTTP://LNK.EXAMPLE/QUELLMONTOUTLOOK</text>

  <!-- info footer -->
  <rect class="info-footer" x="0" y="1095" width="917" height="105" fill="var(--navy)"/>
  <text class="info-lead" x="48" y="1162" font-size="48" textLength="275" lengthAdjust="spacingAndGlyphs">FOR MORE INFO, GO TO</text>
  <text class="info-link" x="338" y="1162" font-size="63" textLength="534" lengthAdjust="spacingAndGlyphs">WWW.QUELLMONTFUTURES.EXAMPLE</text>
</svg>
</body>
</html>
```